Take my logo and make me some cool looking business cards

I've got a logo that we've trademarked so you can't change the logo but you can change it's color combo and find a fun way to incorporate it into a new business card design that is fresh, stylish, and can be applied to some cool medium cost materials (plastic, wood, metal, etc). Basically, we're looking for business cards that stand out in a good way.
Here's the logo we're currently using:
Thanks to everyone that has submitted designs. We've narrowed down to the top 4 designs and tried to eliminate old versions or designs that just didn't match our vision as quickly as we could. We don't plan on keeping this open for the full 9 days; we plan on selecting a design in the next 48 hours; with the goal of having something in the hands of a printer, preferably plastic printer, by Thursday AM Pacific Time.
Business
- must include our existing logo

```html
<!DOCTYPE html>
<html lang="en">
<head>
<meta charset="utf-8">
<title>Tallwind Business Card</title>
<link rel="stylesheet" href="https://fonts.googleapis.com/css2?family=Cinzel:wght@500&family=Open+Sans:wght@400;700&display=swap">
<style>
  :root {
    --canvas: #e9ecef;
    --card-black: #000000;
    --brand-blue: #0a5aa6;
    --accent-blue: #0b86cc;
    --text-white: #ffffff;
  }
  * { margin: 0; padding: 0; box-sizing: border-box; }
  html, body { width: 1200px; height: 1000px; overflow: hidden; background: var(--canvas); }
  .canvas { position: relative; width: 1200px; height: 1000px; }
  .card {
    position: absolute; left: 230px; width: 760px;
    border-radius: 40px; overflow: hidden;
    box-shadow: 2px 3px 4px rgba(0,0,0,0.35);
  }
  .card-front { top: 70px; height: 437px; }
  .card-back { top: 538px; height: 439px; }
  .card-art { position: absolute; inset: 0; display: block; }
  .front-wordmark {
    position: absolute; left: 0; right: 0; top: 172px;
    text-align: center;
    font-family: "Cinzel", serif; font-weight: 500; font-size: 72px;
    letter-spacing: 1px; color: var(--brand-blue);
  }
  .back-wordmark {
    position: absolute; left: 45px; top: 58px;
    font-family: "Open Sans", sans-serif; font-weight: 700; font-size: 52px;
    letter-spacing: -1px; color: var(--brand-blue);
  }
  .contact {
    position: absolute; right: 48px; top: 226px;
    text-align: right; color: var(--text-white);
    font-family: "Open Sans", sans-serif;
  }
  .contact-name { font-size: 26px; line-height: 36px; }
  .contact-role { font-size: 25px; line-height: 36px; margin-bottom: 10px; }
  .contact-line { font-size: 17px; line-height: 26px; }
  .contact-phone { display: inline-flex; align-items: center; gap: 8px; }
  .phone-icon { width: 10px; height: 15px; }
</style>
</head>
<body>
<main class="canvas">
  <section class="card card-front">
    <svg class="card-art" viewBox="0 0 760 437" aria-hidden="true">
      <rect width="760" height="437" fill="var(--brand-blue)"/>
      <path d="M0,190 C70,95 240,25 390,0 H760 V200 C650,340 560,410 440,437 H0 Z" fill="var(--accent-blue)"/>
      <path d="M0,275 C80,125 260,25 440,0 H760 V165 C650,320 520,405 370,437 H0 Z" fill="var(--card-black)"/>
    </svg>
    <div class="front-wordmark">TALLWIND</div>
  </section>

  <section class="card card-back">
    <svg class="card-art" viewBox="0 0 760 439" aria-hidden="true">
      <rect width="760" height="439" fill="var(--brand-blue)"/>
      <path d="M0,0 H565 C520,200 380,370 205,439 H0 Z" fill="var(--accent-blue)"/>
      <path d="M0,0 H540 C495,200 360,360 175,439 H0 Z" fill="var(--card-black)"/>
      <circle class="brand-dot" cx="336" cy="222" r="44" fill="var(--accent-blue)"/>
    </svg>
    <div class="back-wordmark">TALLWIND</div>
    <div class="contact">
      <p class="contact-name">Jordan Hale</p>
      <p class="contact-role">CEO</p>
      <p class="contact-line">412 Marlow Avenue</p>
      <p class="contact-line">Pinecrest, CA 95364</p>
      <p class="contact-line contact-phone">+15550142298
        <svg class="phone-icon" viewBox="0 0 10 15" aria-hidden="true">
          <rect x="0.75" y="0.75" width="8.5" height="13.5" rx="1.5" fill="none" stroke="var(--text-white)" stroke-width="1.5"/>
          <rect x="3.5" y="11" width="3" height="1.3" fill="var(--text-white)"/>
        </svg>
      </p>
    </div>
  </section>
</main>
</body>
</html>
```